E-Learning Directory

It's a library of links to online articles and videos that accompany 10 videos I made for a Venture Pitchcraft Seminar. I'm a newspaper copy-editor who has done some basic page design, so I created a rough idea of how I want these 22 pages to look (incl the placement of royalty-free photos). But it just looks a little flat, tbh. I made it in Mac Pages, but when I converted it to Word, some of the photos got lopped off. But I need it to be in Word and for all the links to be clickable. I'm also a fan of white space. So the brief, basically, is to tidy it up, keep a fair amount of white space, change the fonts to something more reader friendly, and give it more of a professional sheen. I also need to be able to make text edits afterwards myself.

Target Market(s)

Small businesses

Requirements
Must have
• Different size photos (like in PDF)
Nice to have
• White space
Should not have
• Blocky fonts

```html
<!DOCTYPE html>
<html lang="en">
<head>
<meta charset="utf-8">
<title>E-Learning Directory</title>
<link href="https://fonts.googleapis.com/css2?family=Exo+2:wght@700&family=Source+Sans+3:ital,wght@0,200;0,400;0,600;0,700;1,400&display=swap" rel="stylesheet">
<style>
:root{
  --backdrop:#666666;
  --paper:#ffffff;
  --maroon:#8b3a3a;
  --maroon-dark:#6e2b2b;
  --stripe:#dcc0c0;
  --ink:#2b2b2b;
  --link:#1f1aa8;
  --rule:#c9a5a5;
}
*{margin:0;padding:0;box-sizing:border-box}
html,body{width:857px;height:1200px;overflow:hidden;background:var(--backdrop)}
body{position:relative;font-family:"Source Sans 3",sans-serif;color:var(--ink)}
.page{position:absolute;background:var(--paper)}
.cover{left:428.5px;top:76.5px;width:360px;height:508px}
.cover-art{position:absolute;left:0;top:0;width:360px;height:298px;
  background:linear-gradient(180deg,#1b7fb0 0%,#1fa3c4 40%,#7fd0d2 70%,#f4f2d2 100%)}
.cover-heads{position:absolute;left:0;bottom:0;width:360px;height:100px;
  background:linear-gradient(180deg,rgba(10,70,120,0),rgba(14,78,130,.75))}
.brand{position:absolute;left:48px;top:138px;font-family:"Exo 2",sans-serif;font-weight:700;font-size:37px;color:#fff;letter-spacing:.5px;white-space:nowrap}
.cover-title{position:absolute;left:106px;top:320px;font-weight:200;font-size:38.5px;line-height:37px;color:var(--ink);letter-spacing:-.3px}
.cover-sub{position:absolute;left:108px;top:402px;font-weight:700;font-size:9.8px;line-height:12.5px;color:var(--ink)}
.cover-note{position:absolute;left:23.5px;top:466px;width:320px;font-style:italic;font-size:6.3px;line-height:8.3px;color:var(--ink)}
.spread{left:68.6px;top:614.8px;width:719.8px;height:508.7px}
.fold{position:absolute;left:359.9px;top:0;width:1px;height:100%;background:#e4e4e4}
.running-head{position:absolute;top:17px;font-size:4.8px;color:var(--maroon)}
.band{position:absolute;height:20px;
  background:repeating-linear-gradient(135deg,var(--stripe) 0 .7px,transparent .7px 2.4px)}
.section-title{position:absolute;font-weight:700;font-size:12px;color:var(--maroon);white-space:nowrap}
.photo{position:absolute}
.credit{position:absolute;right:34px;bottom:6px;font-size:4px;color:#111}
.body-text{position:absolute;font-size:6.4px;line-height:8.1px;color:var(--ink)}
.body-text b{font-weight:700}
.body-text i{font-style:italic}
.link-row{position:absolute;display:flex;gap:6px;align-items:flex-start}
.link-icon{width:12px;height:10px;flex:none;margin-top:0}
.link{font-size:6.4px;line-height:8.1px;color:var(--link);text-decoration:underline;word-break:break-all}
.folio{position:absolute;width:16px;height:12px;border-radius:3px;background:var(--maroon-dark);color:#fff;font-weight:700;font-size:7.5px;line-height:12px;text-align:center}
.folio-rule{position:absolute;height:.6px;background:var(--rule)}
</style>
</head>
<body>

<section class="page cover">
  <div class="cover-art" role="img" aria-label="Illustration of silhouetted heads in profile beneath speech bubbles filled with connected idea icons">
    <div class="cover-heads"></div>
  </div>
  <div class="brand">Tales for Trade</div>
  <h1 class="cover-title">E-LEARNING<br>DIRECTORY</h1>
  <p class="cover-sub">A Venture Pitchcraft Seminar<br>study aid*</p>
  <p class="cover-note">(*These videos and articles are sourced from external websites and were all checked on May XX, 2022. Talesfortrade.com obviously cannot guarantee they will still be live any time students access them after this date.)</p>
</section>

<section class="page spread">
  <div class="fold"></div>

  <div class="running-head" style="left:26.5px">E-Learning Directory</div>
  <div class="band" style="left:0;top:42.7px;width:359.9px"></div>
  <h2 class="section-title" style="left:33.8px;top:44.5px">Introduction</h2>
  <div class="photo" style="left:34.3px;top:71.2px;width:291.3px;height:249.6px;background:linear-gradient(180deg,#c9d4de 0%,#8a7460 35%,#b39a72 60%,#8b8680 100%)" role="img" aria-label="Photo of a lone walker on a winding road through a mountain valley">
    <span class="credit">Mira Lenko/Stockframe</span>
  </div>
  <div class="band" style="left:34.3px;top:329.8px;width:291.3px;height:7px"></div>
  <p class="body-text" style="left:34.4px;top:356px;width:168px">
    <b>Video:</b> <i>Never underestimate the power of a great story</i><br><br>
    I love this classic ad from French TV station Chaîne Neuf. It’s a very clever introduction to the message behind this course and the tale our protagonist tells is pretty much guaranteed to make you smile. And it’s very hard to argue with the tagline, but maybe I’m biased: “Never underestimate the power of a great story.”
  </p>
  <div class="link-row" style="left:34.4px;top:432px;width:170px">
    <svg class="link-icon" viewBox="0 0 12 10"><path d="M1 5h8M6 2l3 3-3 3" fill="none" stroke="var(--maroon)" stroke-width="1.4" stroke-linecap="round" stroke-linejoin="round"/></svg>
    <span class="link">https://www.videoreel.example/watch?v=Kq7pT2rLmZ</span>
  </div>
  <div class="photo" style="left:207.9px;top:360.2px;width:117.7px;height:77.8px;background:linear-gradient(180deg,#0f1f52 0%,#1b2e6b 55%,#5a4030 85%,#a0603a 100%)" role="img" aria-label="Night photo of a lit triumphal arch with traffic light trails"></div>
  <div class="folio" style="left:34.3px;top:485.3px">2</div>
  <div class="folio-rule" style="left:57px;top:491px;width:268.6px"></div>

  <div class="running-head" style="right:25.5px">A Venture Pitchcraft Seminar study aid</div>
  <div class="band" style="left:359.9px;top:42.7px;width:359.9px"></div>
  <h2 class="section-title" style="left:393.7px;top:44.5px">Objection(s)!</h2>
  <div class="band" style="left:359.9px;top:208.4px;width:359.9px;height:69.7px"></div>
  <div class="photo" style="left:394.2px;top:71.2px;width:291.3px;height:160px;background:radial-gradient(ellipse at 40% 35%,#8a6a5a 0%,#4a3028 40%,#141010 80%)" role="img" aria-label="Close-up photo of a wooden judge’s gavel"></div>
  <h2 class="section-title" style="left:393.7px;top:257px">The Five Myths Holding You Back</h2>

  <p class="body-text" style="left:393.7px;top:303px;width:178px">
    <b>Article:</b> Journaling can do us all some good. Researchers from Westbrook University and Harlan College found that keeping a journal of what you’re thankful for, even if you only write in it once a week for two months, could help you feel happier… and exercise more!
  </p>
  <div class="link-row" style="left:393.7px;top:353px;width:178px">
    <svg class="link-icon" viewBox="0 0 12 10"><path d="M1 5h8M6 2l3 3-3 3" fill="none" stroke="var(--maroon)" stroke-width="1.4" stroke-linecap="round" stroke-linejoin="round"/></svg>
    <span class="link">https://www.dailyledger.example/entry/writing-health-benefits-journal_n_5316270</span>
  </div>
  <div class="photo" style="left:578.9px;top:293.2px;width:106.6px;height:70.7px;background:linear-gradient(135deg,#7d8a5a 0%,#a9a07a 45%,#5f6b3e 100%)" role="img" aria-label="Photo of a person writing in a notebook outdoors on a rock"></div>

  <p class="body-text" style="left:393.7px;top:396px;width:178px">
    <b>Article:</b> Edwin Marlowe, Clara Voss and Tomas Reindl all had access to typewriters… but instead chose to write longhand when they created their works of literary genius.
  </p>
  <div class="link-row" style="left:393.7px;top:430px;width:178px">
    <svg class="link-icon" viewBox="0 0 12 10"><path d="M1 5h8M6 2l3 3-3 3" fill="none" stroke="var(--maroon)" stroke-width="1.4" stroke-linecap="round" stroke-linejoin="round"/></svg>
    <span class="link">https://www.tradeweekly.example/sites/janeharrow/2016/05/15/three-ways-that-writing-with-a-pen-positively-affects-your-brain/?sh=4fb1d2ab8821</span>
  </div>
  <div class="photo" style="left:578.9px;top:382.5px;width:106.6px;height:71.2px;background:linear-gradient(135deg,#9aa0a6 0%,#5c6066 50%,#2e3034 100%)" role="img" aria-label="Photo of hands at a vintage typewriter"></div>

  <div class="folio-rule" style="left:393.7px;top:491px;width:268.6px"></div>
  <div class="folio" style="left:669.5px;top:485.3px">3</div>
</section>

</body>
</html>
```